Logo and Business card design!

Welbrook Estates

We are a Property development and real estate company (needs a logo design).

Welbrook estates is based in Sydney Australia and will be dealing with high net worth individuals with a corporate background. The demographic of clients will be relatively youthful and savvy. We do development finance, property development and some portion of property sales

I'd like the 'Welbrook' part of the name to be strength of the title, with 'property' playing a very minor part, perhaps in tiny font somewhere off to the bottom or side or something

Thank you!

Target Market(s)

25-55 years old

Industry/Entity Type

Real Estate Development

Contact Information for Business Card

Please arrange this information as you see fit

Leon Brightwater
Managing Director
0417 582 273
leon@welbrookestates-example.com.au
www.welbrookestates-example.com.au

Logo Text

Welbrook estates

Font styles to use
Serif

Colors

Designer to choose colors to be used in the design.

Requirements
Must have
• PLEASE VIEW THE UPLOADED IMAGES AND EXAMPLES
• And please put 'property' in small letters at the bottom or to the side. I want it to play a minimalist role, with 'WELBROOK' being the feature
• Colours! Please make sure theyre mostly grey and white with possibly some other dark blue and maybe dark grey
Nice to have
• Please feel free to use whatever colors you like, the suggested colors are something I selected momentarily and dont necessarily reflect strict guidelines
Should not have
• NO pictures or shapes of houses. I dont want the logo design to be so literal in its imagery

```html
<!DOCTYPE html>
<html lang="en">
<head>
<meta charset="utf-8">
<title>Welbrook Estates — Business Card</title>
<link rel="stylesheet" href="https://fonts.googleapis.com/css2?family=Mulish:wght@300;400;700&display=swap">
<style>
  :root {
    --backdrop: #e2e2e2;
    --card-light-top: #ffffff;
    --card-light-bottom: #e9e9e9;
    --card-dark: #38393b;
    --ink-dark: #2b2b2d;
    --ink-mid: #3d3d3f;
    --ink-light: #f2f2f2;
  }
  * { box-sizing: border-box; margin: 0; padding: 0; }
  html, body {
    width: 1200px;
    height: 576px;
    overflow: hidden;
    background: var(--backdrop);
    font-family: "Mulish", "Helvetica Neue", Arial, sans-serif;
  }
  .canvas {
    position: relative;
    width: 1200px;
    height: 576px;
  }
  .card {
    position: absolute;
    top: 138px;
    width: 484px;
    height: 292px;
    border-radius: 14px;
  }
  .card--front {
    left: 82px;
    background: linear-gradient(160deg, var(--card-light-top) 0%, var(--card-light-bottom) 100%);
    color: var(--ink-dark);
  }
  .card--back {
    left: 602px;
    background: var(--card-dark);
    color: var(--ink-light);
  }
  .contact {
    position: absolute;
    left: 32px;
    top: 38px;
    color: var(--ink-mid);
  }
  .contact__name {
    font-size: 18px;
    font-weight: 700;
    color: var(--ink-dark);
    line-height: 1.1;
  }
  .contact__title {
    font-size: 11.5px;
    font-weight: 400;
    margin-top: 2px;
  }
  .contact__details {
    list-style: none;
    margin-top: 14px;
    font-size: 11px;
    line-height: 17px;
  }
  .brand {
    position: absolute;
    display: flex;
    align-items: center;
    gap: 10px;
    font-weight: 300;
  }
  .card--front .brand { left: 32px; bottom: 42px; }
  .card--back .brand { right: 34px; bottom: 42px; }
  .brand__square {
    width: 30px;
    height: 30px;
    background: currentColor;
  }
  .brand__name {
    display: flex;
    flex-direction: column;
    line-height: 1;
  }
  .brand__main {
    font-size: 24px;
    letter-spacing: 1.5px;
  }
  .brand__sub {
    font-size: 9.5px;
    letter-spacing: 6.2px;
    margin-top: 4px;
    padding-left: 2px;
  }
</style>
</head>
<body>
<main class="canvas">
  <section class="card card--front" aria-label="Business card front">
    <div class="contact">
      <p class="contact__name">Leon Brightwater</p>
      <p class="contact__title">Managing Director</p>
      <ul class="contact__details">
        <li>0417 582 273</li>
        <li>leon@welbrookestates-example.com.au</li>
        <li>www.welbrookestates-example.com.au</li>
      </ul>
    </div>
    <div class="brand">
      <span class="brand__square" aria-hidden="true"></span>
      <span class="brand__name">
        <span class="brand__main">WELBROOK</span>
        <span class="brand__sub">ESTATES</span>
      </span>
    </div>
  </section>

  <section class="card card--back" aria-label="Business card back">
    <div class="brand">
      <span class="brand__square" aria-hidden="true"></span>
      <span class="brand__name">
        <span class="brand__main">WELBROOK</span>
        <span class="brand__sub">ESTATES</span>
      </span>
    </div>
  </section>
</main>
</body>
</html>
```